Quiet Willow Business Cards
Quiet Willow Body and Beauty Therapies
Bright & Fun-filled
Noreen Baptiste
Owner/Operator OPV, DRAM, NOPREX, VERTUMA
Bermuda
brightvanspa@examplemail.net
quietwillowvisits.com
Please design a business card with rounded corners Only the logo goes on the front. Name and additional info goes on the back Coloured background please
Noreen Baptiste (in bold print) Owner/Operator OPV, DRAM, NOPREX, VERTUMA mobile: 441-555-0148 email: brightvanspa@examplemail.net web site: quietwillowvisits.com Spa therapies in the comfort of home

```html
<!DOCTYPE html>
<html lang="en">
<head>
<meta charset="utf-8">
<title>Quiet Willow Stationery</title>
<link rel="stylesheet" href="https://fonts.googleapis.com/css2?family=Lora:wght@600&family=Open+Sans:wght@400;700&display=swap">
<style>
  :root {
    --green-dark: #3f6e22;
    --green-mid: #5c8f2e;
    --green-light: #8db55a;
    --green-pale: #e6eedb;
    --paper: #ffffff;
    --frame: #e3e3e3;
    --ink: #5a5a5a;
    --shadow: rgba(0,0,0,0.28);
  }
  * { box-sizing: border-box; margin: 0; padding: 0; }
  html, body { width: 1200px; height: 681px; overflow: hidden; background: var(--paper); }
  .stage {
    position: relative; width: 1200px; height: 681px;
    font-family: "Open Sans", Arial, sans-serif; color: var(--ink);
  }
  .stage-frame {
    position: absolute; left: 19px; top: 19px; width: 1158px; height: 629px;
    border: 1px solid var(--frame);
  }
  .piece {
    position: absolute; background: var(--paper); overflow: hidden;
    box-shadow: 4px 6px 10px var(--shadow);
  }
  .wave-band { position: absolute; left: 0; top: 0; width: 100%; display: block; }

  .brand { position: absolute; display: flex; flex-direction: column; }
  .brand-row { display: flex; align-items: center; gap: 6px; }
  .brand-dot { border-radius: 50%; background: var(--green-mid); flex: none; }
  .brand-name { font-family: "Lora", Georgia, serif; font-weight: 600; color: var(--green-mid); line-height: 1; white-space: nowrap; }
  .brand-tagline { color: var(--green-mid); font-size: 8px; margin-top: 4px; white-space: nowrap; }

  /* Envelope front */
  .envelope-front { left: 60px; top: 67px; width: 497px; height: 240px; }
  .envelope-front .brand { left: 22px; top: 78px; }
  .envelope-front .brand-name { font-size: 26px; }
  .envelope-front .brand-dot { width: 16px; height: 16px; }

  /* Envelope back */
  .envelope-back { left: 60px; top: 336px; width: 497px; height: 235px; }
  .flap { position: absolute; inset: 0; width: 100%; height: 100%; }
  .envelope-back .brand { left: 0; right: 0; top: 70px; align-items: center; }
  .envelope-back .brand-name { font-size: 17px; }
  .envelope-back .brand-dot { width: 11px; height: 11px; }

  /* Letterhead */
  .letterhead { left: 619px; top: 43px; width: 389px; height: 576px; }
  .letterhead .brand { left: 22px; top: 64px; }
  .letterhead .brand-name { font-size: 25px; }
  .letterhead .brand-dot { width: 15px; height: 15px; }
  .letter-contact { position: absolute; left: 22px; top: 130px; font-size: 7.5px; line-height: 1.5; color: var(--green-dark); }
  .letter-watermark {
    position: absolute; left: 0; right: 0; bottom: 70px; text-align: center;
    font-family: "Lora", Georgia, serif; font-weight: 600; font-size: 46px; color: var(--green-pale);
  }

  /* Business cards */
  .card { border-radius: 10px; }
  .card-back { left: 967px; top: 139px; width: 161px; height: 106px; }
  .card-back .brand { left: 10px; top: 26px; }
  .card-back .brand-name { font-size: 12px; }
  .card-back .brand-dot { width: 7px; height: 7px; }
  .card-back .brand-row { gap: 4px; }
  .card-details {
    position: absolute; left: 62px; right: 8px; top: 44px;
    font-size: 4.4px; line-height: 1.5; color: var(--ink); white-space: nowrap;
  }
  .card-name { font-weight: 700; font-size: 5.8px; color: var(--green-dark); }

  .card-front {
    left: 967px; top: 264px; width: 161px; height: 103px;
    background: radial-gradient(ellipse at 40% 40%, var(--green-mid), var(--green-dark));
  }
  .card-front .brand { left: 0; right: 0; top: 30px; align-items: center; }
  .card-front .brand-name { font-size: 15px; color: var(--paper); }
  .card-front .brand-dot { width: 9px; height: 9px; background: var(--paper); }
  .card-front .brand-tagline { color: var(--paper); font-size: 5px; }
  .card-strap { position: absolute; left: 0; right: 0; bottom: 14px; text-align: center; font-size: 4.8px; color: var(--paper); letter-spacing: 0.3px; }
</style>
</head>
<body>
<main class="stage">
  <div class="stage-frame"></div>

  <svg width="0" height="0" style="position:absolute">
    <defs>
      <linearGradient id="band-fill" x1="0" y1="0" x2="1" y2="0">
        <stop offset="0" stop-color="#3f6e22"/>
        <stop offset="0.55" stop-color="#6a9a38"/>
        <stop offset="1" stop-color="#4a7a28"/>
      </linearGradient>
      <symbol id="wave" viewBox="0 0 400 60" preserveAspectRatio="none">
        <path d="M0 0 H400 V26 C300 46 200 14 110 30 C60 39 25 42 0 40 Z" fill="url(#band-fill)"/>
        <path d="M0 34 C70 34 130 20 210 24 S330 40 400 20" fill="none" stroke="#ffffff" stroke-width="2"/>
        <path d="M0 47 C110 46 190 26 280 32 S360 36 400 30" fill="none" stroke="#8db55a" stroke-width="1.5"/>
      </symbol>
    </defs>
  </svg>

  <section class="piece envelope-front">
    <svg class="wave-band" height="70"><use href="#wave" width="100%" height="70"/></svg>
    <div class="brand">
      <div class="brand-row"><span class="brand-dot"></span><span class="brand-name">Quiet Willow</span></div>
      <span class="brand-tagline">Body and Beauty Therapies</span>
    </div>
  </section>

  <section class="piece envelope-back">
    <svg class="flap" viewBox="0 0 497 235" preserveAspectRatio="none">
      <path d="M2 2 L248 92 L495 2" fill="none" stroke="#9a9a9a" stroke-width="1"/>
    </svg>
    <div class="brand">
      <div class="brand-row"><span class="brand-dot"></span><span class="brand-name">Quiet Willow</span></div>
    </div>
  </section>

  <section class="piece letterhead">
    <svg class="wave-band" height="90"><use href="#wave" width="100%" height="90"/></svg>
    <div class="brand">
      <div class="brand-row"><span class="brand-dot"></span><span class="brand-name">Quiet Willow</span></div>
      <span class="brand-tagline">Body and Beauty Therapies</span>
    </div>
    <p class="letter-contact">
      Mobile: 441-555-0148<br>
      Email: brightvanspa@examplemail.net<br>
      quietwillowvisits.com
    </p>
    <div class="letter-watermark">Quiet Willow</div>
  </section>

  <section class="piece card card-back">
    <svg class="wave-band" height="24"><use href="#wave" width="100%" height="24"/></svg>
    <div class="brand">
      <div class="brand-row"><span class="brand-dot"></span><span class="brand-name">Quiet Willow</span></div>
    </div>
    <div class="card-details">
      <div class="card-name">Noreen Baptiste</div>
      Owner/Operator<br>
      OPV, DRAM, NOPREX, VERTUMA<br>
      mobile: 441-555-0148<br>
      email: brightvanspa@examplemail.net<br>
      web site: quietwillowvisits.com
    </div>
  </section>

  <section class="piece card card-front">
    <div class="brand">
      <div class="brand-row"><span class="brand-dot"></span><span class="brand-name">Quiet Willow</span></div>
      <span class="brand-tagline">Body and Beauty Therapies</span>
    </div>
    <p class="card-strap">Spa therapies in the comfort of home</p>
  </section>
</main>
</body>
</html>
```